DPW Business Card

This is a wide-range political consulting firm specializing in high-profile political campaigns. Red should be a predominant color in the business card, since this is a Lantern Party inspired consulting firm, but the word "lantern" will not appear anywhere in any kind of literature. Look has to be clean and crisp. The design should be forward thinking and appropriate for a company that is trying to break away from a traditionally "stodgy" image in politics.

Target Market(s)

potential national political candidates, wealthy donors,

Industry/Entity Type

Political

Contact Information for Business Card

Doran P. Whitcliffe
Political Consultant
437 Orchard Lane SE
#358
Washington, DC 20417

```html
<!DOCTYPE html>
<html lang="en">
<head>
<meta charset="utf-8">
<title>Doran P. Whitcliffe – Business Card</title>
<link rel="stylesheet" href="https://fonts.googleapis.com/css2?family=Roboto+Slab:wght@300;400&display=swap">
<style>
  :root {
    --backdrop: #e7e4e1;
    --card-red-dark: #b80d17;
    --card-red: #cf111c;
    --card-red-light: #df1520;
    --ink-light: #fbf4f2;
    --rule-dark: #5a0a0e;
  }
  html, body {
    margin: 0;
    padding: 0;
    width: 1200px;
    height: 840px;
    overflow: hidden;
    background: var(--backdrop);
  }
  .canvas {
    position: relative;
    width: 1200px;
    height: 840px;
    font-family: "Roboto Slab", Georgia, serif;
    color: var(--ink-light);
  }
  .card {
    position: absolute;
    width: 460px;
    height: 254px;
    background: linear-gradient(200deg, var(--card-red-light) 0%, var(--card-red) 45%, var(--card-red-dark) 100%);
    text-align: center;
  }
  .card--front { left: 74px; top: 219px; }
  .card--back { left: 664px; top: 221px; }
  .card__name {
    position: absolute;
    left: 0; right: 0;
    margin: 0;
    font-weight: 400;
    font-size: 20px;
    letter-spacing: 4.2px;
    text-transform: uppercase;
  }
  .card__title {
    position: absolute;
    left: 0; right: 0;
    margin: 0;
    font-weight: 400;
    font-size: 11.5px;
    letter-spacing: 2.6px;
    text-transform: uppercase;
  }
  .card--front .card__name { top: 97px; }
  .card--front .card__title { top: 127px; }
  .card--back .card__name { top: 109px; }
  .card--back .card__title { top: 139px; }
  .card__rule {
    position: absolute;
    left: 149px;
    top: 155px;
    width: 162px;
    height: 1px;
    background: var(--rule-dark);
  }
  .card__contact {
    position: absolute;
    top: 166px;
    font-size: 11px;
    letter-spacing: 1.4px;
    display: flex;
    align-items: center;
    gap: 5px;
  }
  .card__contact--phone { left: 79px; }
  .card__contact--email { left: 264px; letter-spacing: 0.6px; }
  .card__contact svg { fill: var(--ink-light); }
  .card__address {
    position: absolute;
    left: 0; right: 0;
    top: 191px;
    margin: 0;
    font-style: normal;
    font-size: 11px;
    letter-spacing: 2px;
  }
</style>
</head>
<body>
<main class="canvas">
  <section class="card card--front">
    <h1 class="card__name">Doran P. Whitcliffe</h1>
    <p class="card__title">Political Consultant</p>
    <div class="card__rule"></div>
    <div class="card__contact card__contact--phone">
      <span>+1 123 456 789</span>
      <svg width="10" height="9" viewBox="0 0 10 9" aria-hidden="true">
        <path d="M0 3 Q5 -1 10 3 L10 4 L7.5 4 L7.5 2.8 Q5 2 2.5 2.8 L2.5 4 L0 4 Z"/>
        <path d="M2.5 5 L7.5 5 L9 9 L1 9 Z"/>
      </svg>
    </div>
    <div class="card__contact card__contact--email">
      <svg width="9" height="7" viewBox="0 0 9 7" aria-hidden="true">
        <path d="M0 0 H9 V7 H0 Z" opacity="0.95"/>
        <path d="M0 0 L4.5 4 L9 0" fill="none" stroke="#c8101a" stroke-width="0.9"/>
      </svg>
      <span>info@yoursite.com</span>
    </div>
    <address class="card__address">437 Orchard Lane SE #358 Washington, DC 20417</address>
  </section>

  <section class="card card--back">
    <h2 class="card__name">Doran P. Whitcliffe</h2>
    <p class="card__title">Political Consultant</p>
  </section>
</main>
</body>
</html>
```